bird wings, breathing, coaching, rhythm, heart

I would like this card design to be inspired by the following Rumi poem - now that I see some cards with the poem on it, I am pretty sure I don't want that. The feel of the cards should be watery and emotional, one of rhythm, breathing like a pendulum. An Ouroboros, (alchemical imagery in general), Birds, lungs, bird wings, hands, clouds, water, waves and rivers are all good images. Simple elegance is appreciated.
Cards should contain my name, title (coach), address, phone number and email address.
Your grief for what you've lost lifts a mirror
up to where you're bravely working.
Expecting the worst, you look, and instead,
here's the joyful face you've been wanting to see.
Your hand opens and closes and opens and closes.
If it were always a fist or always stretched open,
you would be paralyzed.
Your deepest presence
is in every small contracting and expanding,
the two as beautifully balanced and coordinated
as birdwings.
Contact Information for Business Card
Torven Maddick, MA
Coach
4817 Quarry Ln.
Berkeley, CA 94703
415-382-6194
maddick@postvine.net
Colors
Designer to choose colors to be used in the design.
Look and feel

```html
<!DOCTYPE html>
<html lang="en">
<head>
<meta charset="utf-8">
<title>Torven Maddick — Business Card</title>
<link href="https://fonts.googleapis.com/css2?family=Italianno&family=Source+Sans+3:wght@400;600&display=swap" rel="stylesheet">
<style>
  :root {
    --backdrop: #2c2c2f;
    --card-dark: #232229;
    --card-dark-edge: #2e2d35;
    --card-light: #ffffff;
    --card-light-shade: #ececec;
    --teal: #3fb7b0;
    --sky: #2aa3d2;
    --leaf: #9cc43c;
    --ink: #1d1d1f;
  }
  * { margin: 0; padding: 0; box-sizing: border-box; }
  html, body {
    width: 1200px; height: 900px; overflow: hidden;
    background: var(--backdrop);
  }
  .canvas {
    position: relative; width: 1200px; height: 900px;
    display: flex; flex-direction: column; align-items: center; justify-content: center;
    gap: 40px;
  }
  .card {
    position: relative; width: 700px; height: 400px;
    border-radius: 22px; overflow: hidden;
  }
  .card--front {
    background: radial-gradient(ellipse at 60% 30%, var(--card-dark-edge), var(--card-dark) 70%);
  }
  .card--back {
    background: linear-gradient(120deg, var(--card-light) 40%, var(--card-light-shade));
  }
  .script-name {
    font-family: "Italianno", cursive; font-weight: 400;
    background: linear-gradient(90deg, var(--teal), var(--leaf));
    -webkit-background-clip: text; background-clip: text;
    color: transparent;
    white-space: nowrap;
  }
  .brand-mark {
    position: absolute; display: flex; align-items: center; gap: 12px;
    font-family: "Italianno", cursive; color: var(--teal);
    white-space: nowrap;
  }
  .brand-mark__dot { border-radius: 50%; background: var(--sky); }

  /* front face */
  .card--front .brand-mark {
    left: 50%; top: 100px; transform: translateX(-50%);
    font-size: 50px;
  }
  .card--front .brand-mark__dot { width: 24px; height: 24px; }
  .card--front .script-name {
    position: absolute; left: 50%; top: 190px; transform: translateX(-50%);
    font-size: 88px; line-height: 1;
  }

  /* back face */
  .card--back .brand-mark {
    left: 50px; top: 150px; font-size: 40px;
  }
  .card--back .brand-mark__dot { width: 20px; height: 20px; }
  .identity {
    position: absolute; left: 300px; top: 40px;
    display: flex; align-items: flex-end; gap: 8px;
  }
  .identity .script-name { font-size: 60px; line-height: 1; }
  .title {
    font-family: "Source Sans 3", sans-serif; font-size: 16px; color: var(--ink);
    line-height: 1.2; padding-bottom: 8px;
  }
  .contact {
    position: absolute; left: 320px; top: 130px; list-style: none;
    font-family: "Source Sans 3", sans-serif; font-size: 18px; color: var(--ink);
  }
  .contact li { display: flex; align-items: center; gap: 12px; height: 30px; white-space: nowrap; }
  .contact svg { width: 16px; height: 16px; fill: var(--sky); flex: none; }
  .wave { position: absolute; left: 0; bottom: 0; width: 700px; height: 400px; }
</style>
</head>
<body>
<main class="canvas">

  <section class="card card--front" aria-label="Card front">
    <div class="brand-mark"><span class="brand-mark__dot"></span>Torven Maddick</div>
    <h1 class="script-name">Torven Maddick</h1>
  </section>

  <section class="card card--back" aria-label="Card back">
    <svg class="wave" viewBox="0 0 700 400" aria-hidden="true">
      <path d="M0,362 C220,345 430,270 570,205 C430,262 220,330 0,345 Z" fill="var(--leaf)"/>
      <path d="M0,378 C210,360 450,275 700,180 L700,400 L0,400 Z" fill="var(--sky)"/>
    </svg>

    <div class="brand-mark"><span class="brand-mark__dot"></span>Torven Maddick</div>

    <div class="identity">
      <h2 class="script-name">Torven Maddick</h2>
      <p class="title">,MA<br>Coach</p>
    </div>

    <ul class="contact">
      <li>
        <svg viewBox="0 0 16 16"><path d="M8 0a5.5 5.5 0 0 0-5.5 5.5C2.5 10 8 16 8 16s5.5-6 5.5-10.5A5.5 5.5 0 0 0 8 0zm0 7.8a2.3 2.3 0 1 1 0-4.6 2.3 2.3 0 0 1 0 4.6z"/></svg>
        4817 Quarry Ln. Berkeley, CA 94703
      </li>
      <li>
        <svg viewBox="0 0 16 16"><path d="M1 5c0-2 3-3 7-3s7 1 7 3v1.5h-3.5V5h-7v1.5H1zM3.5 7h9l2 7h-13zM8 8.5a2.2 2.2 0 1 0 0 4.4 2.2 2.2 0 0 0 0-4.4z"/></svg>
        415-382-6194
      </li>
      <li>
        <svg viewBox="0 0 16 16"><path d="M0 3h16v10H0zm1.5 1.2v.4L8 9l6.5-4.4v-.4z"/></svg>
        maddick@postvine.net
      </li>
    </ul>
  </section>

</main>
</body>
</html>
```